can label designs for Tallow Creek Brewing Company

Tallow Creek Brewing Company will manufacture unique artisan beers in Pawtucket, Rhode Island, starting in the fall of 2018 - be our label designer !!

the word "Tallow" means confident... we want our label designs to portray confidence, and to therefore exude confidence in our customers. we intend our brand to be edgy yet high-end.

This job is for graphic design for our flagship beer, "Chasing Lady Murk", our New England IPA.

New England IPA
“Chasing Lady Murk”
Description: This Hazy IPA will drive you crazy with tons of tropical and citrus aroma. A cloudy straw color is traditional for the beer style. Remember to enjoy beer drink responsibly or have someone give you a lift ;)
8% ABV, 50IBU

Not necessarily to be incorporated into the label design, but the background story behind this beer name is a play on words.. 1) The movie, "rowing past bramble", 2) another name for this type of beer is a "Hazy IPA" . 3) is Our brewer's baby girl's name is Nora- She's a cutie.

We are not certain whether we want the brewery name "Tallow Creek Brewing Company" and logo emphasized, or minimized in favor of the name of the beer and its associated graphics. we would entertain either type of design.

We have 3 other labels to design, and it is likely that we'll use the winning designer for those in order to keep the designs consistent. We want the design of this label to consider that there will be other labels forthcoming and that we'd like some element of consistency from one label to the next - for example, a part of the logo (colors, the rooster head, etc)

one look that we gravitate towards is a dark background with the white version of our logo (see one attachment). possibly each beer label design could be different dark background with same white logo or standalone rooster.

Technicals for this is that it will be used for a 16 ounce can. It also needs to have the required information on it as is described here:
https://www.regsarchive-example.org/cgi-bin/text-idx?SID=4f2a9c7710be33d5a61e08cc2b9f4e07&node=27:1.0.1.1.5&rgn=div5

Here are the requirements in plain english: https://www.printwellpress-example.com/blog/topic/beer-labels

Here's an example of such a label with government requirements:
http://alehousenotes-example.com/wp-content/uploads/2012/09/Twin-Ridge-Bold-Pine-1024x640.jpg

If you need any other information or variations of our logo please let me know. Our instagram site is instagram.com/tallowbrewing if you want to see some other artwork we've created or how our customers interact with us. We are due to open this fall.

Target Market(s)

18-45

Industry/Entity Type

Craft Brewery

Colors

Designer to choose colors to be used in the design.

Requirements
Must have
• logo, either full color, white, or black.
• government requirements for beer labeling
Nice to have
• a means by which this design would tie and carry the brand to subsequent designs - ie all or part of logo, rooster, colors, etc.

```html
<!DOCTYPE html>
<html lang="en">
<head>
<meta charset="utf-8">
<title>Chasing Lady Murk — Tallow Creek Brewing can label</title>
<link rel="stylesheet" href="https://fonts.googleapis.com/css2?family=Oswald:wght@500;600;700&family=Playfair+Display+SC:wght@700;900&display=swap">
<style>
  :root {
    --backdrop: #eef0f1;
    --label-light: #74ad46;
    --label-mid: #5e9a38;
    --label-dark: #4b8430;
    --forest: #1f4a1e;
    --band: #2b5a22;
    --band-edge: #9ccb6a;
    --ink-white: #ffffff;
    --spec-green: #b9e07e;
    --scene-tone-a: #496f31;
    --scene-tone-b: #3b5f29;
  }
  * { box-sizing: border-box; margin: 0; padding: 0; }
  html, body {
    width: 1200px;
    height: 990px;
    overflow: hidden;
    background: var(--backdrop);
  }
  .canvas {
    position: relative;
    width: 1200px;
    height: 990px;
    background: radial-gradient(ellipse at 50% 45%, #f9fafa 0%, var(--backdrop) 70%);
  }
  .label {
    position: absolute;
    left: 456px;
    top: 80px;
    width: 288px;
    height: 730px;
    overflow: hidden;
    background: linear-gradient(180deg, var(--label-light) 0%, var(--label-mid) 55%, var(--label-dark) 100%);
  }
  .brand {
    position: absolute;
    top: 92px;
    left: 0;
    width: 100%;
    display: flex;
    align-items: center;
    justify-content: center;
    gap: 14px;
  }
  .brand-mark {
    width: 46px;
    height: 46px;
    border-radius: 50%;
    background: var(--forest);
  }
  .brand-name {
    font-family: "Oswald", sans-serif;
    font-weight: 700;
    font-size: 54px;
    line-height: 1;
    letter-spacing: 1px;
    color: var(--forest);
    text-transform: uppercase;
  }
  .brand-sub {
    position: absolute;
    top: 156px;
    left: 0;
    width: 100%;
    text-align: center;
    padding-left: 60px;
    font-family: "Oswald", sans-serif;
    font-weight: 700;
    font-size: 22px;
    letter-spacing: 5px;
    color: var(--forest);
  }
  .beer-name {
    position: absolute;
    top: 290px;
    left: 0;
    width: 100%;
    text-align: center;
    font-family: "Playfair Display SC", serif;
    font-weight: 900;
    color: var(--ink-white);
    line-height: 0.95;
    text-shadow: 2px 2px 0 var(--forest);
  }
  .beer-name .line-one { display: block; font-size: 52px; }
  .beer-name .line-two { display: block; font-size: 52px; }
  .scene-art {
    position: absolute;
    top: 430px;
    left: 0;
    width: 100%;
    height: 190px;
    background: radial-gradient(ellipse at 55% 50%, var(--scene-tone-a) 0%, var(--scene-tone-b) 55%, rgba(75,132,48,0) 80%);
    opacity: 0.85;
  }
  .style-band {
    position: absolute;
    left: 0;
    bottom: 0;
    width: 100%;
    height: 150px;
  }
  .style-band svg { position: absolute; inset: 0; }
  .style-name {
    position: absolute;
    top: 62px;
    width: 100%;
    text-align: center;
    font-family: "Oswald", sans-serif;
    font-weight: 600;
    font-size: 27px;
    letter-spacing: 0.5px;
    color: var(--ink-white);
  }
  .specs {
    position: absolute;
    top: 104px;
    width: 100%;
    display: flex;
    justify-content: center;
    gap: 26px;
    font-family: "Oswald", sans-serif;
    font-weight: 500;
    font-size: 14px;
    color: var(--spec-green);
  }
</style>
</head>
<body>
  <main class="canvas">
    <section class="label">
      <div class="brand">
        <span class="brand-mark"></span>
        <span class="brand-name">Tallow</span>
      </div>
      <div class="brand-sub">BREWING</div>

      <h1 class="beer-name">
        <span class="line-one">Chasing</span>
        <span class="line-two">Lady Murk</span>
      </h1>

      <div class="scene-art" role="img" aria-label="Faded illustration of a vintage sedan in dark green tones"></div>

      <div class="style-band">
        <svg width="288" height="150" viewBox="0 0 288 150" aria-hidden="true">
          <path d="M0 48 Q144 20 288 48 L288 150 L0 150 Z" fill="var(--band)"/>
          <path d="M0 48 Q144 20 288 48" fill="none" stroke="var(--band-edge)" stroke-width="2"/>
        </svg>
        <div class="style-name">NEW ENGLAND IPA</div>
        <div class="specs">
          <span>16 Oz | 500 mL</span>
          <span>8% ABV | 50 IBU</span>
        </div>
      </div>
    </section>
  </main>
</body>
</html>
```